HRB Business Advisors Corporate Stationery

A Corporate Stationery Design is required for HRB Business Advisors - Chartered Accountants. The Design is to incorporate Black and Navy Blue and is to give an example of the following: Letterhead/DL Envelope/With Compliment Slip/Business Card and Binding Covers.

Industry/Entity Type

Business

Requirements
Must have
• The Corporate Stationery has the following compulsory attributes:

Logo (Refer File) - words underneath Chartered Accountants
ABN 42 315 870 916
Street Address: Level 4/27 Marlowe St Melbourne VIC
Postal Address: PO Box 24739 Fenwick St East Melbourne VIC 8003
Telephone: 03 9482 3026
Facsimile: 03 9482 3059
Directors: Dorian Pike Kevin Alder Marisa Holt

```html
<!DOCTYPE html>
<html lang="en">
<head>
<meta charset="utf-8">
<title>HRB Business Advisors – Corporate Stationery</title>
<link rel="stylesheet" href="https://fonts.googleapis.com/css2?family=Questrial&family=Arimo:wght@400;700&display=swap">
<style>
  :root {
    --navy: #15307c;
    --blue: #1f5fbf;
    --charcoal: #333639;
    --muted: #6b6e72;
    --rule: #9aa3b5;
    --paper: #ffffff;
    --backdrop: #e3e4e6;
    --sig-tone: #eceef1;
  }
  * { box-sizing: border-box; margin: 0; padding: 0; }
  html, body { width: 1200px; height: 720px; overflow: hidden; }
  body {
    background: var(--backdrop);
    font-family: "Arimo", Arial, sans-serif;
    color: var(--charcoal);
    position: relative;
  }
  .sheet {
    position: absolute;
    background: var(--paper);
    box-shadow: 0 2px 8px rgba(0,0,0,.12);
  }

  /* Brand lockup */
  .brand { display: flex; align-items: center; gap: 8px; color: var(--navy); font-family: "Questrial", Arial, sans-serif; font-weight: 400; }
  .brand-mark { width: 34px; height: 34px; background: var(--navy); flex: none; }
  .brand-text { line-height: 1; }
  .brand-name { font-size: 30px; letter-spacing: 1px; display: block; }
  .brand-sub { font-size: 10px; display: block; margin-top: 2px; }
  .brand--small .brand-mark { width: 22px; height: 22px; }
  .brand--small .brand-name { font-size: 19px; }
  .brand--small .brand-sub { font-size: 7px; }

  /* Contact block */
  .contact { display: flex; gap: 8px; align-items: flex-start; }
  .contact-feature { background: var(--navy); flex: none; }
  .contact-list { list-style: none; border-left: 1px solid var(--rule); padding-left: 7px; font-size: 7px; line-height: 1.55; color: var(--charcoal); }
  .contact-list li { display: flex; align-items: center; gap: 4px; white-space: nowrap; }
  .contact-list svg { width: 7px; height: 7px; fill: var(--navy); flex: none; }

  /* Letterhead */
  .letterhead { left: 40px; top: 63px; width: 420px; height: 594px; padding: 34px 34px 30px; }
  .letterhead .date { position: absolute; right: 34px; top: 26px; font-size: 10px; color: var(--navy); display: flex; gap: 6px; align-items: flex-end; }
  .letterhead .date-line { width: 80px; border-bottom: 1px solid var(--navy); height: 9px; }
  .letterhead .brand { margin-top: 22px; }
  .letter-body { margin-top: 26px; font-size: 8px; line-height: 1.5; text-align: justify; }
  .letter-body p + p { margin-top: 10px; }
  .letter-sign { position: absolute; left: 34px; bottom: 34px; font-size: 12px; line-height: 1.25; }
  .signature { width: 90px; height: 46px; background: var(--sig-tone); margin-top: 6px; }
  .letterhead .contact { position: absolute; right: 30px; bottom: 70px; }
  .letterhead .contact-feature { width: 92px; height: 92px; }

  /* Business cards */
  .card { width: 200px; height: 104px; left: 960px; padding: 12px; }
  .card--front { top: 63px; }
  .card--front .brand { margin-top: 20px; }
  .card--front .card-meta { position: absolute; right: 12px; top: 12px; font-size: 6px; text-align: right; line-height: 1.5; color: var(--muted); }
  .card--back { top: 179px; }
  .card-person { color: var(--navy); font-family: "Questrial", Arial, sans-serif; }
  .card-person strong { font-size: 12px; font-weight: 400; display: block; }
  .card-person span { font-size: 7px; color: var(--muted); }
  .card--back .contact { position: absolute; right: 10px; bottom: 10px; }
  .card--back .contact-feature { width: 40px; height: 40px; }
  .card--back .contact-list { font-size: 5.5px; }
  .card--back .contact-list svg { width: 5.5px; height: 5.5px; }

  /* DL envelope */
  .envelope { left: 500px; top: 63px; width: 440px; height: 220px; padding: 22px; }
  .envelope .brand { position: absolute; left: 22px; bottom: 40px; }
  .envelope .contact { position: absolute; right: 22px; top: 22px; }
  .envelope .contact-feature { width: 54px; height: 54px; }

  /* Compliments slip */
  .slip { left: 500px; top: 307px; width: 660px; height: 350px; padding: 30px; }
  .slip .brand { position: absolute; left: 30px; bottom: 60px; }
  .slip-title { position: absolute; right: 30px; top: 34px; font-family: "Arimo", Arial, sans-serif; font-weight: 700; font-size: 17px; color: var(--navy); }
  .slip .contact { position: absolute; right: 30px; top: 110px; }
  .slip .contact-feature { width: 80px; height: 80px; }
  .slip .contact-list { font-size: 8px; }
  .slip .contact-list svg { width: 8px; height: 8px; }
</style>
</head>
<body>

<svg width="0" height="0" style="position:absolute" aria-hidden="true">
  <symbol id="i-home" viewBox="0 0 10 10"><path d="M5 1 L10 5 H8.5 V9.5 H6 V6.5 H4 V9.5 H1.5 V5 H0 Z"/></symbol>
  <symbol id="i-mail" viewBox="0 0 10 10"><path d="M0 2 H10 V8.5 H0 Z M0.8 2.6 L5 5.6 L9.2 2.6 V2.6 Z" fill-rule="evenodd"/></symbol>
  <symbol id="i-phone" viewBox="0 0 10 10"><path d="M2 0.5 L4 2.5 L3 4 Q4.5 6 6 7 L7.5 6 L9.5 8 L8 9.5 Q3 9 0.5 2 Z"/></symbol>
  <symbol id="i-fax" viewBox="0 0 10 10"><path d="M2.5 0.5 H7.5 V3 H9.5 V8 H7.5 V9.5 H2.5 V8 H0.5 V3 H2.5 Z M3.5 6 V8.5 H6.5 V6 Z" fill-rule="evenodd"/></symbol>
  <symbol id="i-at" viewBox="0 0 10 10"><path d="M5 0.5 A4.5 4.5 0 1 0 8.5 8 L7.7 7.2 A3.4 3.4 0 1 1 8.4 5 V5.6 Q8.4 6.6 7.6 6.6 Q6.8 6.6 6.8 5.6 V3 H5.8 V3.4 A2 2 0 1 0 6 6.8 Q6.6 7.6 7.6 7.6 Q9.5 7.6 9.5 5.2 A4.5 4.5 0 0 0 5 0.5 Z M5 3.9 A1.1 1.1 0 1 1 5 6.1 A1.1 1.1 0 1 1 5 3.9 Z" fill-rule="evenodd"/></symbol>
  <symbol id="i-web" viewBox="0 0 10 10"><path d="M5 0.5 A4.5 4.5 0 1 0 5 9.5 A4.5 4.5 0 1 0 5 0.5 Z M5 1.5 A3.5 3.5 0 0 1 8.5 5 H1.5 A3.5 3.5 0 0 1 5 1.5 Z" fill-rule="evenodd"/></symbol>
</svg>

<!-- Letterhead -->
<section class="sheet letterhead" aria-label="Letterhead">
  <div class="date">Date <span class="date-line"></span></div>
  <div class="brand">
    <span class="brand-mark"></span>
    <span class="brand-text"><span class="brand-name">HRB</span><span class="brand-sub">Business Advisors Pty Ltd</span></span>
  </div>
  <div class="letter-body">
    <p>Lorem ipsum dolor sit amet, consectetuer adipiscing elit. Nam cursus. Morbi ut mi. Nullam enim leo, egestas id, condimentum at, laoreet mattis, massa. Sed eleifend nonummy diam. Praesent mauris ante, elementum et, bibendum at, posuere sit amet, nibh. Duis tincidunt lectus quis dui viverra vestibulum. Suspendisse vulputate aliquam dui. Nulla elementum dui ut augue. Aliquam vehicula mi at mauris. Maecenas placerat, nisl at consequat rhoncus, sem nunc gravida justo, quis eleifend arcu velit quis lacus. Morbi magna magna, tincidunt a, mattis non, imperdiet vitae, tellus. Sed odio est, auctor ac, sollicitudin in, consequat vitae, orci. Fusce id felis. Vivamus sollicitudin metus eget eros. Pellentesque habitant morbi tristique senectus et netus et malesuada fames ac turpis egestas. In posuere felis nec tortor. Pellentesque faucibus. Ut accumsan ultricies elit.</p>
    <p>Duis quam. Nam eget lacus. Aliquam erat volutpat. Quisque dignissim congue leo. Lorem ipsum dolor sit amet, consectetuer adipiscing elit. Nam cursus. Morbi ut mi. Nullam enim leo, egestas id, condimentum at, laoreet mattis, massa. Sed eleifend nonummy diam. Praesent mauris ante, elementum et, bibendum at, posuere sit amet, nibh. Duis tincidunt lectus quis dui viverra vestibulum. Suspendisse vulputate aliquam dui. Nulla elementum dui ut augue. Aliquam vehicula mi at mauris. Maecenas placerat, nisl at consequat rhoncus, sem nunc gravida justo, quis eleifend arcu velit quis lacus.</p>
    <p>Pellentesque habitant morbi tristique senectus et netus et malesuada fames ac turpis egestas. Pellentesque faucibus. Ut accumsan ultricies elit. Maecenas at justo id velit placerat molestie. Cras a ante vitae enim iaculis aliquam. Mauris nunc quam, venenatis nec, euismod sit amet, egestas placerat, est. Curabitur et malesuada fames ac turpis egestas. Cras id elit. Integer quis urna. Ut ante enim, dapibus malesuada, fringilla eu, condimentum quis, tellus. Aenean porttitor eros vel dolor. Donec convallis pede venenatis nibh.</p>
  </div>
  <div class="letter-sign">
    Regards<br>Dorian Pike
    <div class="signature" role="img" aria-label="Handwritten signature of Dorian Pike"></div>
  </div>
  <div class="contact">
    <span class="contact-feature"></span>
    <ul class="contact-list">
      <li><svg><use href="#i-home"/></svg>Level 4/27 Marlowe St Melbourne VIC</li>
      <li><svg><use href="#i-mail"/></svg>PO Box 24739 Fenwick St East</li>
      <li><svg><use href="#i-mail"/></svg>East Melbourne VIC 8003</li>
      <li><svg><use href="#i-phone"/></svg>03 9482 3026</li>
      <li><svg><use href="#i-fax"/></svg>03 9482 3059</li>
      <li><svg><use href="#i-at"/></svg>info@hrbadvisors.com.au</li>
      <li><svg><use href="#i-web"/></svg>www.hrbadvisors.com.au</li>
    </ul>
  </div>
</section>

<!-- Business card front -->
<section class="sheet card card--front" aria-label="Business card front">
  <div class="card-meta">ABN 42 315 870 916<br>www.hrbadvisors.com.au</div>
  <div class="brand brand--small">
    <span class="brand-mark"></span>
    <span class="brand-text"><span class="brand-name">HRB</span><span class="brand-sub">Business Advisors Pty Ltd</span></span>
  </div>
</section>

<!-- Business card back -->
<section class="sheet card card--back" aria-label="Business card back">
  <div class="card-person"><strong>Dorian Pike</strong><span>Director</span></div>
  <div class="contact">
    <span class="contact-feature"></span>
    <ul class="contact-list">
      <li><svg><use href="#i-home"/></svg>Level 4/27 Marlowe St Melbourne VIC</li>
      <li><svg><use href="#i-mail"/></svg>PO Box 24739 Fenwick St East VIC 8003</li>
      <li><svg><use href="#i-phone"/></svg>03 9482 3026</li>
      <li><svg><use href="#i-fax"/></svg>03 9482 3059</li>
      <li><svg><use href="#i-at"/></svg>info@hrbadvisors.com.au</li>
      <li><svg><use href="#i-web"/></svg>www.hrbadvisors.com.au</li>
    </ul>
  </div>
</section>

<!-- DL envelope -->
<section class="sheet envelope" aria-label="DL envelope">
  <div class="contact">
    <span class="contact-feature"></span>
    <ul class="contact-list">
      <li><svg><use href="#i-home"/></svg>Level 4/27 Marlowe St Melbourne VIC</li>
      <li><svg><use href="#i-mail"/></svg>PO Box 24739 Fenwick St East VIC 8003</li>
      <li><svg><use href="#i-phone"/></svg>03 9482 3026</li>
      <li><svg><use href="#i-fax"/></svg>03 9482 3059</li>
      <li><svg><use href="#i-web"/></svg>www.hrbadvisors.com.au</li>
    </ul>
  </div>
  <div class="brand">
    <span class="brand-mark"></span>
    <span class="brand-text"><span class="brand-name">HRB</span><span class="brand-sub">Business Advisors Pty Ltd</span></span>
  </div>
</section>

<!-- Compliments slip -->
<section class="sheet slip" aria-label="With compliments slip">
  <h2 class="slip-title">With Compliments</h2>
  <div class="contact">
    <span class="contact-feature"></span>
    <ul class="contact-list">
      <li><svg><use href="#i-home"/></svg>Level 4/27 Marlowe St Melbourne VIC</li>
      <li><svg><use href="#i-mail"/></svg>PO Box 24739 Fenwick St East</li>
      <li><svg><use href="#i-mail"/></svg>East Melbourne VIC 8003</li>
      <li><svg><use href="#i-phone"/></svg>03 9482 3026</li>
      <li><svg><use href="#i-fax"/></svg>03 9482 3059</li>
      <li><svg><use href="#i-at"/></svg>info@hrbadvisors.com.au</li>
      <li><svg><use href="#i-web"/></svg>www.hrbadvisors.com.au</li>
    </ul>
  </div>
  <div class="brand">
    <span class="brand-mark"></span>
    <span class="brand-text"><span class="brand-name">HRB</span><span class="brand-sub">Business Advisors Pty Ltd</span></span>
  </div>
</section>

</body>
</html>
```